Webdesign for blog, vlog and website
The designs for my website were better than what I expected when I started this contest. I knew I needed a call-to-action on my homepage, but I thought it wouldn't be possible and I didn't ask for it either. But Anselmo did it anyway. Furthermore, his design looked very good. For that reason I selected him as winner already before I should. I am very happy.

```html
<!DOCTYPE html>
<html lang="en">
<head>
<meta charset="utf-8">
<title>Ideora – Mobile Homepage</title>
<link rel="stylesheet" href="https://fonts.googleapis.com/css2?family=Open+Sans:wght@300;400;600;700&display=swap">
<style>
  :root {
    --stage: #e9eaee;
    --white: #ffffff;
    --ink: #1b1b2e;
    --brand: #1f1fd6;
    --hero: #8a86d8;
    --hero-deep: #5a52cf;
    --muted: #6d6d80;
    --card: #2ea6e3;
    --card-deep: #2a8fd0;
    --rule: #d9d9e4;
  }
  * { box-sizing: border-box; margin: 0; padding: 0; }
  html, body { width: 1200px; height: 801px; overflow: hidden; }
  body {
    background: var(--stage);
    font-family: "Open Sans", Arial, sans-serif;
    color: var(--ink);
    display: flex; align-items: center; justify-content: center;
  }
  .screen {
    width: 350px; height: 740px;
    background: var(--white);
    overflow: hidden;
    display: flex; flex-direction: column;
    box-shadow: 0 10px 40px rgba(20,20,60,.18);
  }
  .status-bar {
    height: 22px; flex: none; background: var(--white);
    display: flex; align-items: center; justify-content: space-between;
    padding: 0 10px; font-size: 11px; font-weight: 600;
  }
  .status-bar .carrier { display: flex; align-items: center; gap: 5px; }
  .status-bar .dots { display: flex; gap: 2px; }
  .status-bar .dot { width: 6px; height: 6px; border-radius: 50%; background: var(--ink); }
  .status-bar .dot.off { background: none; border: 1px solid var(--ink); }
  .site-header {
    height: 68px; flex: none; background: var(--white);
    display: flex; align-items: center; justify-content: space-between;
    padding: 0 16px;
    border-bottom: 3px solid var(--brand);
  }
  .brand { display: flex; align-items: center; gap: 8px; }
  .brand-mark { width: 22px; height: 22px; border-radius: 50%; background: var(--brand); }
  .brand-name { font-size: 24px; font-weight: 700; color: var(--brand); line-height: 1; }
  .menu-toggle { display: flex; flex-direction: column; gap: 4px; }
  .menu-toggle span { width: 22px; height: 3px; background: var(--brand); border-radius: 2px; }
  .hero {
    position: relative; height: 400px; flex: none;
    padding: 70px 26px 0; color: var(--white);
  }
  .hero-art {
    position: absolute; inset: 0;
    background: linear-gradient(150deg, var(--hero-deep) 0%, var(--hero) 45%, var(--hero) 70%, var(--hero-deep) 100%);
  }
  .hero-content { position: relative; }
  .hero-title { font-size: 40px; font-weight: 300; line-height: 1.1; }
  .hero-subtitle { margin-top: 14px; font-size: 16px; font-weight: 400; letter-spacing: 2px; }
  .search { margin-top: 30px; display: flex; flex-direction: column; gap: 16px; align-items: flex-start; }
  .search-field {
    width: 100%; height: 40px; background: var(--white);
    padding: 0 12px; font-size: 12px; color: var(--muted);
    display: flex; align-items: center;
  }
  .search-button {
    width: 120px; height: 38px; border: 1px solid var(--white); border-radius: 4px;
    display: flex; align-items: center; justify-content: center;
    font-size: 14px; color: var(--white);
  }
  .entries { padding: 18px 20px 14px; text-align: center; flex: none; }
  .entries-icon { width: 34px; height: 22px; margin: 0 auto 12px; display: block; }
  .entries-tabs { display: flex; justify-content: center; gap: 10px; font-size: 10px; color: var(--muted); }
  .entries-tabs .active { color: var(--brand); font-weight: 600; border-bottom: 2px solid var(--brand); }
  .entries-tabs .sep { color: var(--rule); }
  .post-card { flex: 1; background: linear-gradient(135deg, var(--card), var(--card-deep)); }
</style>
</head>
<body>
  <main class="screen">
    <div class="status-bar">
      <div class="carrier">
        <div class="dots"><i class="dot"></i><i class="dot"></i><i class="dot off"></i><i class="dot off"></i><i class="dot off"></i></div>
        NOVA
        <svg width="12" height="9" viewBox="0 0 12 9"><path d="M1 3a7 7 0 0 1 10 0M3 5a4 4 0 0 1 6 0M6 8l1-1a1.4 1.4 0 0 0-2 0z" stroke="#1b1b2e" stroke-width="1.3" fill="none"/></svg>
      </div>
      <span>2:14 PM</span>
      <svg width="22" height="10" viewBox="0 0 22 10"><rect x="0.5" y="0.5" width="18" height="9" rx="2" fill="none" stroke="#1b1b2e"/><rect x="2" y="2" width="14" height="6" fill="#1b1b2e"/><rect x="19.5" y="3" width="2" height="4" fill="#1b1b2e"/></svg>
    </div>
    <header class="site-header">
      <div class="brand">
        <span class="brand-mark"></span>
        <span class="brand-name">Ideora</span>
      </div>
      <div class="menu-toggle"><span></span><span></span><span></span></div>
    </header>
    <section class="hero">
      <div class="hero-art" role="img" aria-label="Illustration of light bulbs and graduation caps in shades of blue and violet"></div>
      <div class="hero-content">
        <h1 class="hero-title">Believes and Convictions</h1>
        <p class="hero-subtitle">WHAT'S YOUR IDEAS?</p>
        <div class="search">
          <div class="search-field">Search News or Blog</div>
          <div class="search-button">Search</div>
        </div>
      </div>
    </section>
    <section class="entries">
      <svg class="entries-icon" viewBox="0 0 34 22"><path d="M17 1 33 8 17 15 1 8z" fill="#4038c8"/><path d="M8 11v6c3 3 15 3 18 0v-6l-9 4z" fill="#4038c8"/><path d="M31 9v8" stroke="#4038c8" stroke-width="1.5"/></svg>
      <div class="entries-tabs">
        <span class="active">10 ENTRIES</span><span class="sep">|</span>
        <span>20 ENTRIES</span><span class="sep">|</span>
        <span>30 ENTRIES</span>
      </div>
    </section>
    <div class="post-card" role="img" aria-label="Featured blog post photo of a person against a blue background"></div>
  </main>
</body>
</html>
```